7 Loop Flyer

We are a gym named Korvalle and we need a flyer design for our challenge we will be having called the '7 LOOP'. The '7 LOOP' is a 6 Week Transformation Challenge where participants will train throughout the 6 weeks then see what progress they have made at the end, with prizes on offer for the best results.

We would like to see designs that use the colour blue.

The design we would like has been sketched and added in files section, subject to minor word changes later on. Both logos have also been added to the file section as well. As per the sketch, At the top should be the 'Korvalle 7 LOOP' logo. Underneath will have writing that says 'A 6 week transformation challenge that will get you in the best shape of your life!

Below that will say 'NO EGOS REAL PEOPLE REAL RESULTS' underneath each other. With 'ENTRIES NOW OPEN' below.

Then at the bottom the other Korvalle logo.

Colors
33a6d7
85cae6
0292cd
0355a3
3276b5
85abd2
e667a6
e34197

Requirements
Must have
• Mention of the prizes
• "Chance to win over $1200 in prizes"
• 1st Place $600 CASH MONEY!!!!
• Sign up now kicks off September 22
• The ultimate 6 Week Transformation
Should not have
• Generic / Stock images

```html
<!DOCTYPE html>
<html lang="en">
<head>
<meta charset="utf-8">
<title>Korvalle 7 LOOP – 6 Week Transformation Challenge</title>
<link rel="stylesheet" href="https://fonts.googleapis.com/css2?family=Anton&family=Montserrat:wght@400;600;700&family=Roboto+Condensed:wght@400;700;800&display=swap">
<style>
  :root {
    --page: #e6e6e6;
    --paper-light: #ffffff;
    --navy: #0c3f8a;
    --navy-deep: #0b2f6a;
    --blue: #1d5dab;
    --cyan: #33b5df;
    --lime: #dcf51a;
    --ink: #111111;
    --white: #ffffff;
  }
  html, body {
    margin: 0;
    width: 1200px;
    height: 1200px;
    overflow: hidden;
    background: var(--page);
  }
  .flyer {
    position: absolute;
    left: 172px;
    top: 0;
    width: 856px;
    height: 1200px;
    display: block;
  }
  .font-display { font-family: 'Anton', Impact, sans-serif; }
  .font-body { font-family: 'Montserrat', Arial, sans-serif; }
  .font-condensed { font-family: 'Roboto Condensed', 'Arial Narrow', sans-serif; }
  .brand-name { fill: var(--navy-deep); }
  .brand-dot { fill: var(--cyan); }
  .headline-main { fill: url(#headline-fill); stroke: var(--lime); stroke-width: 5; paint-order: stroke; }
  .headline-sub { fill: var(--navy); }
  .tagline-pill { fill: var(--cyan); }
  .tagline-text { fill: var(--white); font-weight: 700; }
  .values { fill: var(--ink); font-weight: 600; }
  .values-divider { fill: var(--blue); }
  .prize-ring { fill: none; stroke: var(--cyan); stroke-width: 3; }
  .prize-disc { fill: url(#disc-fill); }
  .prize-lead { fill: var(--white); font-weight: 700; }
  .prize-total { fill: var(--lime); }
  .prize-foot { fill: var(--white); font-weight: 400; }
  .first-label { fill: var(--blue); font-weight: 800; }
  .first-amount { fill: var(--navy); }
  .cash { fill: var(--cyan); font-weight: 700; }
  .kickoff-band { fill: var(--lime); }
  .kickoff-lead { fill: var(--ink); font-weight: 700; }
  .kickoff-date { fill: var(--navy); }
  .call-halo { fill: var(--paper-light); stroke: var(--cyan); stroke-width: 3; }
  .call-disc { fill: var(--cyan); }
  .call-text { fill: var(--white); }
  .footer-tag { fill: var(--navy-deep); font-weight: 400; }
</style>
</head>
<body>
<svg class="flyer" viewBox="0 0 918 1288" xmlns="http://www.w3.org/2000/svg" aria-label="Korvalle 7 LOOP six week transformation challenge flyer">
  <defs>
    <radialGradient id="paper-fill" cx="0.5" cy="0.18" r="0.8">
      <stop offset="0" stop-color="#ffffff"/>
      <stop offset="1" stop-color="#eeeeee"/>
    </radialGradient>
    <linearGradient id="headline-fill" x1="0" y1="0" x2="0" y2="1">
      <stop offset="0" stop-color="#2366bb"/>
      <stop offset="1" stop-color="#0c3f8a"/>
    </linearGradient>
    <radialGradient id="disc-fill" cx="0.5" cy="0.5" r="0.55">
      <stop offset="0" stop-color="#2a6bbd"/>
      <stop offset="1" stop-color="#0d3f88"/>
    </radialGradient>
  </defs>

  <rect class="paper" width="918" height="1288" fill="url(#paper-fill)"/>

  <!-- Challenge brand -->
  <g class="brand-top">
    <circle class="brand-dot" cx="290" cy="166" r="14"/>
    <text class="brand-name font-display" x="478" y="185" font-size="50" text-anchor="middle">KORVALLE 7 LOOP</text>
  </g>

  <!-- Headline -->
  <text class="headline-main font-display" x="68" y="501" font-size="232" textLength="787" lengthAdjust="spacingAndGlyphs">A 6 WEEK</text>
  <text class="headline-sub font-display" x="68" y="581" font-size="69" textLength="787" lengthAdjust="spacingAndGlyphs">TRANSFORMATION CHALLENGE</text>

  <rect class="tagline-pill" x="70" y="606" width="793" height="53" rx="26"/>
  <text class="tagline-text font-condensed" x="466" y="645" font-size="36" text-anchor="middle" textLength="760" lengthAdjust="spacingAndGlyphs">that will get you in the best shape of your life!</text>

  <g class="values font-body" font-size="30">
    <text x="78" y="701" textLength="155" lengthAdjust="spacingAndGlyphs">NO EGOS</text>
    <rect class="values-divider" x="266" y="676" width="4" height="30"/>
    <text x="303" y="701" textLength="232" lengthAdjust="spacingAndGlyphs">REAL PEOPLE</text>
    <rect class="values-divider" x="568" y="676" width="4" height="30"/>
    <text x="600" y="701" textLength="250" lengthAdjust="spacingAndGlyphs">REAL RESULTS</text>
  </g>

  <!-- Total prizes -->
  <g class="prize-pool">
    <circle class="prize-ring" cx="257" cy="967" r="243"/>
    <circle class="prize-disc" cx="257" cy="967" r="230"/>
    <text class="prize-lead font-body" x="260" y="834" font-size="44" text-anchor="middle">Chance</text>
    <text class="prize-lead font-body" x="260" y="882" font-size="44" text-anchor="middle">to win over</text>
    <text class="prize-total font-display" x="67" y="1059" font-size="170" textLength="380" lengthAdjust="spacingAndGlyphs">$1200</text>
    <text class="prize-foot font-body" x="255" y="1118" font-size="42" text-anchor="middle" textLength="228" lengthAdjust="spacingAndGlyphs">IN PRIZES</text>
  </g>

  <!-- First prize -->
  <text class="first-label font-condensed" x="480" y="790" font-size="54" textLength="216" lengthAdjust="spacingAndGlyphs">1st Prize</text>
  <text class="first-amount font-display" x="553" y="933" font-size="150" textLength="297" lengthAdjust="spacingAndGlyphs">$600</text>
  <text class="cash font-body" x="560" y="980" font-size="33" textLength="303" lengthAdjust="spacingAndGlyphs">CASH MONEY!!!!</text>

  <!-- Kick-off -->
  <rect class="kickoff-band" x="500" y="1001" width="418" height="141"/>
  <text class="kickoff-lead font-condensed" x="543" y="1047" font-size="36" textLength="322" lengthAdjust="spacingAndGlyphs">Sign up now kicks off</text>
  <text class="kickoff-date font-display" x="608" y="1112" font-size="46" textLength="259" lengthAdjust="spacingAndGlyphs">SEPTEMBER 22</text>

  <!-- Call -->
  <g class="call">
    <circle class="call-halo" cx="493" cy="1164" r="114"/>
    <circle class="call-disc" cx="493" cy="1164" r="102"/>
    <text class="call-text font-display" x="493" y="1151" font-size="37" text-anchor="middle" textLength="108" lengthAdjust="spacingAndGlyphs">CALL US</text>
    <text class="call-text font-display" x="493" y="1192" font-size="34" text-anchor="middle" textLength="166" lengthAdjust="spacingAndGlyphs">0491 570 156</text>
  </g>

  <!-- Gym brand -->
  <g class="brand-footer">
    <text class="brand-name font-display" x="793" y="1207" font-size="38" text-anchor="middle" textLength="172" lengthAdjust="spacingAndGlyphs">KORVALLE</text>
    <text class="footer-tag font-condensed" x="793" y="1229" font-size="15" text-anchor="middle">PERSONAL &amp;</text>
    <text class="footer-tag font-condensed" x="793" y="1246" font-size="15" text-anchor="middle">GROUP TRAINING</text>
  </g>
</svg>
</body>
</html>
```